10' WIDE TRADE SHOW BACKDROP DESIGN

I need a 10' wide by 7'4" tall trade show back drop designed for my company. We are a carpet cleaning company. It is a display from brio displays and you can see the dimensions here.
http://www.briodisplays-demo.com/quick-textile-stand-spare-prints.html

I will supply logo, ps art of some dogs we use as well as a picture of our van so you can match it a little. From there I need something very cool.

I will supply them via filehopper-demo.com because the files are large.

Our website is www.gleamrugworks-demo.com if you would like to see a little about our company.

The final design should use our blue colors, emphasize Safer, Cleaner, Faster, Smarter. It should bring home the fact that we are a quality cleaner not a cheap cleaner.

Target Market(s)

Mid to high end home and business owners who will make decisions on floor cleaning

Industry/Entity Type

Trade

Colors
0455a3
3276b5
0592cd
34a7d8
86cae6
86acd3
ffffff

Requirements
Must have
• Logo + "Safer, Cleaner, Faster, Smarter"
Dalmation pic
website
"FREE CLEANING" ask for details
Nice to have
• should incorporate the feel of the van so I have included a couple of pictures of it.

```html
<!DOCTYPE html>
<html lang="en">
<head>
<meta charset="utf-8">
<title>Gleam Rugworks – Trade Show Backdrop</title>
<link href="https://fonts.googleapis.com/css2?family=Roboto+Condensed:wght@400;700&display=swap" rel="stylesheet">
<style>
  :root {
    --stage: #e4e6e8;
    --brand-blue: #0592cd;
    --brand-blue-deep: #0a7fc0;
    --cap-blue: #0b86c6;
    --brand-sky: #86cae6;
    --headline-band: rgba(120,120,120,0.55);
    --frame-light: #dfeef6;
    --text-light: #f2f4f5;
    --text-dark: #2b2b2b;
  }
  * { margin: 0; padding: 0; box-sizing: border-box; }
  html, body {
    width: 1200px; height: 880px; overflow: hidden;
    background: var(--stage);
    font-family: "Roboto Condensed", Arial, sans-serif;
  }
  .end-cap {
    position: absolute; top: 40px; height: 800px;
    background: linear-gradient(180deg, var(--brand-blue) 0%, var(--brand-blue-deep) 100%);
    color: var(--text-light); font-weight: 700;
    overflow: hidden;
  }
  .end-cap-left { left: 40px; width: 24px; background: linear-gradient(180deg, #e9e9e8 0%, #e9e9e8 62%, var(--brand-blue) 62%, var(--cap-blue) 100%); }
  .end-cap-right { left: 1064px; width: 72px; background: linear-gradient(180deg, var(--cap-blue) 0%, var(--brand-blue-deep) 100%); border-left: 1px solid rgba(255,255,255,0.25); }
  .cap-text {
    position: absolute; white-space: nowrap;
    transform-origin: 0 0; transform: rotate(90deg);
  }
  .end-cap-left .cap-text { left: 18px; top: 560px; font-size: 12px; letter-spacing: 0.5px; opacity: 0.9; }
  .end-cap-right .cap-text { left: 60px; top: 230px; font-size: 20px; line-height: 25px; }
  .backdrop {
    position: absolute; left: 64px; top: 40px;
    width: 1000px; height: 800px;
    background: linear-gradient(180deg, var(--brand-blue) 0%, var(--brand-blue-deep) 100%);
    overflow: hidden;
  }
  .backdrop-art { position: absolute; inset: 0; }
  .headline {
    position: absolute; left: 100px; top: 42px; width: 640px;
    text-align: center; color: var(--text-light);
    font-weight: 700; font-size: 35px; line-height: 49px; letter-spacing: 0.5px;
  }
  .brand {
    position: absolute; left: 110px; top: 418px; width: 440px;
    display: flex; align-items: center; justify-content: center; gap: 14px;
    color: var(--brand-sky); font-weight: 700; font-size: 40px; letter-spacing: 2px;
  }
  .brand-square { width: 24px; height: 24px; background: var(--brand-sky); flex: none; }
  .brand-site {
    position: absolute; left: 110px; top: 476px; width: 440px;
    text-align: center; color: var(--text-dark);
    font-weight: 700; font-size: 28px;
  }
  .phone {
    position: absolute; left: 660px; top: 480px; width: 320px;
    text-align: center; color: var(--text-light); font-weight: 700;
  }
  .phone-word { font-size: 40px; line-height: 44px; }
  .phone-digits { font-size: 22px; line-height: 26px; }
  .pitch {
    position: absolute; left: 0; top: 598px; width: 1000px;
    text-align: center; color: var(--text-light);
  }
  .pitch-line { font-size: 25px; line-height: 34px; }
  .pitch-points { font-weight: 700; font-size: 25px; line-height: 34px; }
  .pitch-points .dot { margin: 0 18px; }
</style>
</head>
<body>
  <aside class="end-cap end-cap-left">
    <span class="cap-text">www.grimyrugs-demo.com</span>
  </aside>

  <main class="backdrop">
    <svg class="backdrop-art" viewBox="0 0 1000 800" width="1000" height="800">
      <defs>
        <linearGradient id="roomTone" x1="0" y1="0" x2="0" y2="1">
          <stop offset="0" stop-color="#b9b9b7"/>
          <stop offset="0.3" stop-color="#dcdcda"/>
          <stop offset="0.45" stop-color="#f3f3f1"/>
          <stop offset="0.6" stop-color="#e6e4e0"/>
          <stop offset="0.75" stop-color="#b8b4ae"/>
          <stop offset="1" stop-color="#cfcfcc"/>
        </linearGradient>
      </defs>
      <path class="photo-frame"
            d="M0,0 L752,0 C848,60 878,200 814,326 C742,468 566,574 300,574 C180,574 60,558 0,544 Z"
            fill="var(--frame-light)"/>
      <path class="photo-area" role="img"
            aria-label="Photo of a bright white living room with sofas, and a row of dalmatian puppies sitting on a spotted carpet"
            d="M0,0 L738,0 C830,60 860,200 800,320 C730,458 560,560 300,560 C180,560 60,545 0,530 Z"
            fill="url(#roomTone)"/>
      <path class="headline-band" d="M0,36 L790,36 C812,70 820,110 818,140 L0,140 Z"
            fill="var(--headline-band)"/>
    </svg>

    <h1 class="headline">DO YOUR FLOORS OR UPHOLSTERY<br>HAVE YOU SEEING SPOTS ?</h1>

    <div class="brand"><span class="brand-square"></span><span>GLEAM RUGWORKS</span></div>
    <div class="brand-site">www.grimyrugs-demo.com</div>

    <div class="phone">
      <div class="phone-word">1-555-SO-GRIMY</div>
      <div class="phone-digits">1-555-764-7469</div>
    </div>

    <div class="pitch">
      <p class="pitch-line">GREEN CARPET &amp; UPHOLSTERY CLEANING THAT IS SAFER FOR YOUR FAMILY</p>
      <p class="pitch-points"><span class="dot">•</span>DRY IN 1 HOUR<span class="dot">•</span>PET ODOR REMOVAL<span class="dot">•</span>COLORED STAIN REMOVAL</p>
    </div>
  </main>

  <aside class="end-cap end-cap-right">
    <span class="cap-text">Book Online, 24/7 at<br>www.gleamrugworks-demo.com</span>
  </aside>
</body>
</html>
```